Business Card Design Project for - The Pellowick Greenworks Company Ltd. We are a Landscape and garden

I would like designer to use all special glosses etc so i can have a professional looking business card. The theme of the business card can reflect that of the Logo attached by MarkQuarry or your own unique ideas.. please feel free to go wild as i hope i can select a winner i like - my budget will be committed so please get involved. Good luck and thank you Lyndon

Target Market(s)

Must look Professional

General Public and Businesses including Councils, Local Government, Hospitals, Hotels, Professionals and Professional Sports People.

Industry/Entity Type

Landscape Gardening

Contact Information for Business Card

The Pellowick Greenworks Company Ltd

Mr L.R Ashcombe
Head Office - Quayfront Park Manchester
t. 0772 408 916
e. info@pellowickgreenworks.co.uk
w. www.pellowickgreenworks.co.uk

Facebook - https://www.friendpage-example.com/ThePellowickGreenworksCompany/
Twitter - https://chirpline-example.com/ThePruningCart
Instagram - https://www.snapgrid-example.com/thepellowickgreenworkscompany/?hl=en
Google+ - https://circles.searchhub-example.com/u/0/208473950162438571093
Yelp - https://www.reviewnook-example.co.uk/biz/the-pellowick-greenworks-company-manchester-4

Font styles to use
Serif
Script
Other font styles liked:
• I don't have much of an idea of font types sorry

Colors

Designer to choose colors to be used in the design.

Requirements
Must have
• A Professional look and Design
• Special effects with gloss and fading of colours possibly..
• Front and back design
Nice to have
• All special features with effects and gloss etc

```html
<!DOCTYPE html>
<html lang="en">
<head>
<meta charset="utf-8">
<title>The Pellowick Greenworks Company Ltd – Business Card</title>
<link rel="stylesheet" href="https://fonts.googleapis.com/css2?family=Cinzel:wght@400;600&family=Open+Sans:wght@400;600;700&display=swap">
<style>
  :root {
    --stage: #d9d9d9;
    --card-dark: #231f20;
    --card-light: #ffffff;
    --green: #3dbb3a;
    --green-deep: #2a9a2a;
    --brand-grey: #8a8a8a;
    --ink: #1a1a1a;
    --muted: #9a9a9a;
  }
  * { box-sizing: border-box; margin: 0; padding: 0; }
  html, body { width: 1200px; height: 876px; overflow: hidden; }
  body { background: var(--stage); position: relative; font-family: "Open Sans", sans-serif; }

  .card {
    position: absolute;
    width: 560px;
    height: 340px;
    overflow: hidden;
    box-shadow: 0 6px 18px rgba(0,0,0,0.25);
  }
  .card--front { left: 70px; top: 80px; background: var(--card-dark); }
  .card--back { left: 570px; top: 456px; background: var(--card-light); }

  .rule { position: absolute; left: 0; right: 0; height: 3px; background: var(--green); }
  .card--front .rule--top { top: 18px; }
  .card--front .rule--bottom { bottom: 18px; }

  .band { position: absolute; left: 0; right: 0; height: 12px; background: var(--card-dark); }
  .band--top { top: 0; }
  .band--bottom { bottom: 0; }
  .card--back .rule--top { top: 12px; }
  .card--back .rule--bottom { bottom: 12px; }

  .brand { position: absolute; text-align: center; font-family: "Cinzel", serif; color: var(--brand-grey); }
  .brand__dot { display: block; margin: 0 auto 14px; border-radius: 50%; background: var(--green); }
  .brand__name { display: block; font-weight: 400; letter-spacing: 0.04em; white-space: nowrap; }
  .brand__sub { display: block; letter-spacing: 0.22em; white-space: nowrap; }

  .card--front .brand { left: 0; right: 0; top: 92px; }
  .card--front .brand__dot { width: 64px; height: 64px; }
  .card--front .brand__name { font-size: 40px; }
  .card--front .brand__sub { font-size: 14px; margin-top: 6px; }

  .card--back .brand { left: 26px; width: 240px; top: 118px; }
  .card--back .brand__dot { width: 42px; height: 42px; margin-bottom: 10px; }
  .card--back .brand__name { font-size: 24px; }
  .card--back .brand__sub { font-size: 8.5px; margin-top: 4px; letter-spacing: 0.2em; }

  .person { position: absolute; left: 300px; top: 52px; width: 240px; }
  .person__name { font-size: 21px; font-weight: 700; color: var(--ink); }
  .person__role { font-size: 16px; color: var(--muted); letter-spacing: 0.2em; margin-top: -2px; }
  .person__rule { height: 2px; background: var(--green); margin-top: 6px; }

  .contact { position: absolute; left: 300px; top: 170px; list-style: none; }
  .contact__row { display: flex; align-items: center; gap: 10px; height: 22px; font-size: 12.5px; color: var(--ink); }
  .contact__icon { width: 18px; height: 18px; background: var(--green); border-radius: 2px; display: flex; align-items: center; justify-content: center; }
  .contact__icon svg { width: 12px; height: 12px; }
  .contact__office { font-weight: 700; font-size: 13px; margin-top: 4px; }

  .social { position: absolute; left: 300px; top: 272px; }
  .social__icons { display: flex; gap: 4px; }
  .social__icon { width: 13px; height: 13px; background: var(--muted); border-radius: 2px; }
  .social__handle { font-size: 12.5px; color: var(--muted); margin-top: 2px; }
</style>
</head>
<body>

  <section class="card card--front" aria-label="Card front">
    <div class="rule rule--top"></div>
    <div class="brand">
      <span class="brand__dot"></span>
      <span class="brand__name">THE PELLOWICK</span>
      <span class="brand__sub">GREENWORKS COMPANY LTD</span>
    </div>
    <div class="rule rule--bottom"></div>
  </section>

  <section class="card card--back" aria-label="Card back">
    <div class="band band--top"></div>
    <div class="rule rule--top"></div>

    <div class="brand">
      <span class="brand__dot"></span>
      <span class="brand__name">THE PELLOWICK</span>
      <span class="brand__sub">GREENWORKS COMPANY LTD</span>
    </div>

    <div class="person">
      <p class="person__name">Mr L.R Ashcombe</p>
      <p class="person__role">general director</p>
      <div class="person__rule"></div>
    </div>

    <ul class="contact">
      <li class="contact__row">
        <span class="contact__icon"><svg viewBox="0 0 12 12"><rect x="3.5" y="1" width="5" height="10" rx="1" fill="none" stroke="#fff" stroke-width="1.2"/><circle cx="6" cy="9.3" r="0.7" fill="#fff"/></svg></span>
        0772 408 916
      </li>
      <li class="contact__row">
        <span class="contact__icon"><svg viewBox="0 0 12 12"><rect x="1" y="2.5" width="10" height="7" fill="none" stroke="#fff" stroke-width="1.2"/><path d="M1 2.5 L6 7 L11 2.5" fill="none" stroke="#fff" stroke-width="1.2"/></svg></span>
        info@pellowickgreenworks.co.uk
      </li>
      <li class="contact__row">
        <span class="contact__icon"><svg viewBox="0 0 12 12"><circle cx="6" cy="6" r="4.8" fill="none" stroke="#fff" stroke-width="1.1"/><ellipse cx="6" cy="6" rx="2" ry="4.8" fill="none" stroke="#fff" stroke-width="1"/><line x1="1.2" y1="6" x2="10.8" y2="6" stroke="#fff" stroke-width="1"/></svg></span>
        www.pellowickgreenworks.co.uk
      </li>
      <li class="contact__row contact__office">Head Office - Quayfront Park Manchester</li>
    </ul>

    <div class="social">
      <div class="social__icons">
        <span class="social__icon"></span>
        <span class="social__icon"></span>
        <span class="social__icon"></span>
        <span class="social__icon"></span>
        <span class="social__icon"></span>
      </div>
      <p class="social__handle">ThePellowickGreenworksCompany</p>
    </div>

    <div class="rule rule--bottom"></div>
    <div class="band band--bottom"></div>
  </section>

</body>
</html>
```